Re-design a website for a millionaire mentor

We need an expert website designer to re-design the website vKeenstride.net

The website would have 4 pages. A home page, Summit Circle page, Hire RM page and an About page.

Here are some reference websites

https://www.lumovance.net
https://rolfbanter.net/

I will also attach a beginning of mockup of the home page I did myself to give an idea of the style we like, please use the quote "If you are not chasing your potential you are wasting your life" instead of the one in the current website...

You don't have the use the mockup (just the quote) and are free to use all your creativity.

Target Market(s)

Entrepreneurs

Number of Pages Required

4 page

Font styles to use
Other font styles liked:
• Franklin Gothic

Requirements
Must have
• -Call of action on the main page to download a free business plan
• -Hire rm page check out reference: http://www.hiremarkbellow.net
• -summit circle page with a button to sign in or join the summit circle. Check out reference for example: https://www.lumovance.net/glide_academy

```html
<!DOCTYPE html>
<html lang="en">
<head>
<meta charset="utf-8">
<title>vKeenstride — Home</title>
<link rel="stylesheet" href="https://fonts.googleapis.com/css2?family=Oswald:wght@400;500;600&family=Montserrat:wght@400;500;600;700;800&family=Open+Sans:ital,wght@0,400;0,600;0,700;1,400;1,600&family=Libre+Franklin:wght@400;600;700;800&display=swap">
<style>
:root{
  --red:#e0222a;
  --red-dark:#b5141b;
  --red-deep:#8f0f14;
  --ink:#1c1c1c;
  --dark:#1e1e20;
  --text:#4a4a4a;
  --muted:#8a8a8a;
  --line:#d6d6d6;
  --white:#ffffff;
  --pale:#f1f1f1;
  --gold:#f2c21a;
}
*{box-sizing:border-box;margin:0;padding:0}
html,body{width:1200px;height:4072px;overflow:hidden}
body{position:relative;background:var(--white);font-family:"Open Sans",sans-serif;color:var(--text)}
.abs{position:absolute}
section,header,footer{position:absolute;left:0;width:1200px;overflow:hidden}

/* hero */
.hero{top:0;height:795px;background:var(--dark)}
.hero-photo{position:absolute;inset:0;background:radial-gradient(ellipse at 78% 45%,#4a4a4e 0%,#2a2a2d 35%,#161618 75%)}
.hero-speaker{position:absolute;left:690px;top:140px;width:360px;height:545px;background:linear-gradient(180deg,#3a2e2a 0%,#1b1b1d 60%,#121213 100%);border-radius:160px 160px 0 0;opacity:.85}
.brand{position:absolute;display:flex;align-items:center;gap:10px;font-family:"Oswald",sans-serif;font-weight:600;color:var(--white);letter-spacing:1px}
.brand-mark{width:26px;height:26px;background:var(--red)}
.hero .brand{left:145px;top:40px;font-size:34px}
.ask{left:652px;top:33px;color:#ddd;font-size:16px}
.phone{left:640px;top:52px;color:var(--white);font-family:"Libre Franklin",sans-serif;font-size:27px;font-weight:600}
.phone-icon{left:822px;top:35px;width:44px;height:44px;border:2px solid var(--white);border-radius:50%}
.btn{position:absolute;display:flex;align-items:center;justify-content:center;background:var(--red);color:var(--white);font-family:"Montserrat",sans-serif;font-weight:600;border-radius:22px}
.quote-btn{left:888px;top:35px;width:168px;height:44px;font-size:17px}
.nav{position:absolute;top:110px;right:145px;display:flex;gap:24px;font-family:"Montserrat",sans-serif;font-weight:700;font-size:15.5px;color:var(--white)}
.headline{left:145px;top:255px;font-family:"Oswald",sans-serif;font-size:34px;line-height:55px;color:var(--white);text-transform:uppercase}
.headline em{color:var(--red);font-style:italic;font-weight:400;text-transform:none;font-size:36px}
.plan{left:147px;top:375px;color:#e6e6e6;font-style:italic;font-size:20px}
.click-btn{left:145px;top:443px;width:173px;height:44px;font-size:17px;font-weight:700}
.arrow-nav{position:absolute;top:345px}
.newsletter-bar{position:absolute;left:0;top:680px;width:1200px;height:115px;background:rgba(10,10,10,.55)}
.nl-title{left:130px;top:703px;font-family:"Montserrat",sans-serif;font-weight:700;font-size:26px;color:var(--white)}
.nl-sub{left:130px;top:737px;font-size:14px;font-style:italic;color:#ccc}
.nl-label{top:692px;font-family:"Montserrat",sans-serif;font-weight:600;font-size:14px;color:var(--white)}
.field{position:absolute;background:var(--white);border:1px solid #ccc;font-size:12px;color:#777;padding:0 12px;display:flex;align-items:center}
.nl-btn{left:910px;top:720px;width:155px;height:36px;border-radius:0;font-size:15px;font-weight:700}

/* welcome */
.welcome{top:795px;height:600px;background:var(--pale)}
.tilt-frame{position:absolute;background:var(--white);border:5px solid #3a1420;box-shadow:0 6px 14px rgba(0,0,0,.25)}
.welcome h2{position:absolute;left:577px;top:98px;font-family:"Montserrat",sans-serif;font-weight:700;font-size:44px;color:var(--ink)}
.welcome h2 span{color:var(--red);font-weight:500}
.welcome p{position:absolute;left:577px;top:170px;width:470px;font-size:15px;line-height:27px}
.read-btn{position:absolute;left:577px;top:385px;width:129px;height:38px;border:2px solid var(--red);border-radius:20px;color:var(--red);font-family:"Montserrat",sans-serif;font-weight:600;font-size:15px;display:flex;align-items:center;justify-content:center}

/* services */
.services{top:1350px;height:640px}
.section-title{position:absolute;left:0;width:1200px;text-align:center;font-family:"Montserrat",sans-serif;font-size:38px;color:var(--ink)}
.section-title b{font-weight:800}
.services .section-title{top:122px;color:var(--white)}
.services .section-title b{color:var(--white)}
.divider{position:absolute;left:540px;width:120px;height:12px}
.service{position:absolute;top:240px;width:300px;text-align:center;color:var(--white)}
.service .icon{width:100px;height:100px;margin:0 auto;border-radius:50%;background:var(--gold);display:flex;align-items:center;justify-content:center}
.service h3{margin-top:22px;font-family:"Montserrat",sans-serif;font-weight:600;font-size:23px}
.service p{margin-top:14px;font-size:14.5px;line-height:24px;color:#f7dcdc}

/* quote form */
.request{top:1990px;height:652px;background:var(--white)}
.request-photo{position:absolute;left:600px;top:0;width:600px;height:652px;background:linear-gradient(90deg,#fff 0%,#c9d6e2 14%,#8ea3b6 45%,#5f6f80 100%)}
.request-person{position:absolute;left:760px;top:40px;width:280px;height:612px;border-radius:140px 140px 0 0;background:linear-gradient(180deg,#3b2c26 0%,#1d2433 45%,#181c26 100%)}
.request h2{position:absolute;left:142px;top:50px;font-family:"Montserrat",sans-serif;font-size:40px;color:var(--ink);font-weight:400}
.request h2 b{font-weight:800}
.form-label{position:absolute;left:142px;font-size:15px;color:#333}
.form-input{position:absolute;left:142px;width:465px;height:44px;border:1px solid #bbb;background:var(--white)}
.submit-btn{left:142px;top:2518px;width:223px;height:40px;border-radius:2px;font-size:16px;font-weight:700}

/* news */
.news{top:2642px;height:624px;background:var(--white)}
.news .section-title{top:70px}
.news-card{position:absolute;top:205px;width:270px;text-align:center}
.news-card .tilt-frame{position:relative;width:262px;height:210px;margin:0 auto;border:5px solid var(--red)}
.news-card h3{margin-top:28px;font-family:"Montserrat",sans-serif;font-weight:700;font-size:16px;line-height:27px;color:var(--ink)}
.news-date{margin-top:10px;display:flex;justify-content:center;align-items:center;gap:8px;color:var(--red);font-family:"Montserrat",sans-serif;font-weight:700;font-size:14px}

/* testimonial */
.testimonial{top:3266px;height:337px;background:#222224}
.avatar{position:absolute;left:257px;top:79px;width:176px;height:176px;border-radius:50%;border:4px solid var(--white);background:radial-gradient(circle at 50% 40%,#8a5a46 0%,#5b3a2e 45%,#2b2b2d 100%)}
.testimonial blockquote{position:absolute;left:508px;top:84px;width:460px;font-style:italic;font-size:16.5px;line-height:28px;color:#e6e6e6}
.author{position:absolute;left:508px;top:205px;font-family:"Montserrat",sans-serif;font-weight:600;font-size:16px;line-height:28px;color:var(--white)}
.qmark{position:absolute;font-family:"Oswald",sans-serif;font-size:90px;color:var(--white);line-height:1}

/* footer */
.site-footer{top:3603px;height:347px;background:var(--white);border-top:1px solid #eee}
.site-footer .brand{left:142px;top:90px;font-size:34px;color:var(--ink)}
.social{position:absolute;top:205px;width:34px;height:34px;border:1.5px solid #333;border-radius:50%}
.foot-title{position:absolute;top:58px;font-family:"Montserrat",sans-serif;font-weight:700;font-size:22px;color:var(--ink)}
.foot-item{position:absolute;left:360px;display:flex;gap:14px;font-size:13px;line-height:18px;color:#333}
.foot-item svg{flex:none}
.foot-text{position:absolute;left:610px;top:108px;width:250px;font-size:12.5px;line-height:19px;color:#444}
.foot-input{position:absolute;left:610px;top:168px;width:272px;height:38px;border:1px solid #bbb;border-radius:20px;font-size:12px;color:#777;padding-left:14px;display:flex;align-items:center}
.foot-btn{left:610px;top:3822px;width:138px;height:36px;border-radius:18px;font-size:15px;font-weight:700}
.quick{position:absolute;left:923px;top:110px;list-style:none;font-size:14px;line-height:25px;color:#333}
.copyright{top:3950px;height:122px;background:var(--white);border-top:1px solid #e5e5e5;text-align:center;padding-top:50px;font-size:14px;color:#333}
</style>
</head>
<body>

<header class="hero">
  <div class="hero-photo" role="img" aria-label="Dark stage photo of the mentor speaking into a microphone"></div>
  <div class="hero-speaker" role="img" aria-label="Mentor in a black jacket gesturing while speaking"></div>
  <div class="brand"><span class="brand-mark"></span>KEENSTRIDE</div>
  <div class="abs ask">Have any Question?</div>
  <div class="abs phone">(08) 4410 5120</div>
  <div class="abs phone-icon">
    <svg width="40" height="40" viewBox="0 0 40 40"><path d="M14 11c1-1 2-1 3 0l2 3c.6 1 .4 2-.4 2.6l-1.4 1c1 2.4 2.8 4.3 5 5.4l1.1-1.4c.6-.8 1.7-1 2.6-.4l3 2c1 .7 1 1.8 0 2.8l-1.5 1.5c-1.4 1.3-4 1-7-1.2-3.3-2.4-6-5.6-7.3-8.8-1-2.6-1-4.6.2-5.8z" fill="#fff"/></svg>
  </div>
  <div class="btn quote-btn">Get a Quote</div>
  <nav class="nav"><span>HOME</span><span>SUMMIT CIRCLE</span><span>HIRE RM</span><span>ABOUT US</span><span>CONTACT US</span></nav>

  <h1 class="abs headline">If you are not chasing your <em>Potential</em><br>you are <em>Wasting</em> your life</h1>
  <div class="abs plan">Download My Free Business Plan</div>
  <div class="btn click-btn">CLICK HERE »</div>
  <svg class="abs" style="left:350px;top:410px" width="100" height="80" viewBox="0 0 100 80"><path d="M92 6C70 30 45 50 12 62" stroke="#e0222a" stroke-width="4" fill="none" stroke-linecap="round"/><path d="M26 48L10 63l22 3" stroke="#e0222a" stroke-width="4" fill="none" stroke-linecap="round" stroke-linejoin="round"/></svg>
  <svg class="arrow-nav" style="left:92px" width="20" height="34" viewBox="0 0 20 34"><path d="M16 3L4 17l12 14" stroke="#fff" stroke-width="3" fill="none"/></svg>
  <svg class="arrow-nav" style="left:1088px" width="20" height="34" viewBox="0 0 20 34"><path d="M4 3l12 14L4 31" stroke="#fff" stroke-width="3" fill="none"/></svg>

  <div class="newsletter-bar"></div>
  <div class="abs nl-title">JOIN OUR NEWSLETTER</div>
  <div class="abs nl-sub">Sed ut perspiciatis unde omnis iste natus</div>
  <div class="abs nl-label" style="left:490px">Name</div>
  <div class="abs nl-label" style="left:697px">Email</div>
  <div class="field" style="left:490px;top:720px;width:192px;height:36px">Your Name Here</div>
  <div class="field" style="left:697px;top:720px;width:193px;height:36px">Your Mail Address</div>
  <div class="btn nl-btn">SUBSCRIBE</div>
</header>

<section class="welcome">
  <div class="tilt-frame" style="left:168px;top:105px;width:345px;height:335px;transform:rotate(-6deg)">
    <div role="img" aria-label="Mentor presenting on stage beside a projected slide" style="position:absolute;inset:14px;background:linear-gradient(90deg,#2a2224 0%,#5d4a46 45%,#d9d4cc 75%,#efece6 100%)"></div>
  </div>
  <h2>Welcome to <span>vKeenstride</span></h2>
  <p>Sed ut perspiciatis unde omnis iste natus error sit voluptatem accusantium doloremque laudantium, totam rem aperiam, eaque ipsa quae ab illo inventore veritatis et quasi architecto beatae vitae dicta sunt explicabo. Nemo enim ipsam voluptatem quia voluptas sit aspernatur aut odit aut fugit, sed quia consequuntur et quasi architecto beatae vitae dicta sunt explicabo</p>
  <div class="read-btn">Read More</div>
</section>

<section class="services">
  <svg class="abs" style="left:0;top:0" width="1200" height="640" viewBox="0 0 1200 640">
    <defs><linearGradient id="svcBg" x1="0" y1="0" x2="0" y2="1"><stop offset="0" stop-color="#d8242b"/><stop offset="1" stop-color="#c81c23"/></linearGradient></defs>
    <polygon points="0,55 330,2 1200,120 1200,640 0,640" fill="url(#svcBg)"/>
    <polygon points="0,55 330,2 260,62 0,110" fill="#9e1118"/>
    <polygon points="330,2 1200,120 1200,150 420,60" fill="#b5141b" opacity=".7"/>
  </svg>
  <div class="abs" role="img" aria-label="Faint city skyline behind the services" style="left:0;top:170px;width:1200px;height:470px;background:linear-gradient(180deg,rgba(120,10,15,0) 0%,rgba(120,10,15,.25) 100%)"></div>
  <h2 class="section-title"><b>OUR</b> SERVICES</h2>
  <svg class="divider" style="top:187px" viewBox="0 0 120 12"><line x1="8" y1="6" x2="112" y2="6" stroke="#fff" stroke-width="2"/><circle cx="6" cy="6" r="4" fill="none" stroke="#fff" stroke-width="2"/><circle cx="114" cy="6" r="4" fill="none" stroke="#fff" stroke-width="2"/></svg>

  <div class="service" style="left:130px">
    <div class="icon"><svg width="54" height="54" viewBox="0 0 54 54" fill="none" stroke="#2a2a2a" stroke-width="2.4"><circle cx="27" cy="15" r="8"/><path d="M13 40c0-8 6-13 14-13s14 5 14 13"/><rect x="8" y="38" width="38" height="10"/></svg></div>
    <h3>Leadership Conference</h3>
    <p>Sed ut perspiciatis unde omnis iste natus error sit voluptatem accusantium doque laudantium, totam rem aperiam, eaque ipsa quae ab illo inventore veritatis et quasi architecto beatae</p>
  </div>
  <div class="service" style="left:448px">
    <div class="icon"><svg width="54" height="54" viewBox="0 0 54 54" fill="none" stroke="#2a2a2a" stroke-width="2.4"><rect x="9" y="11" width="36" height="24" rx="2"/><path d="M4 42h46l-4-7H8z"/></svg></div>
    <h3>Books &amp; Interviews</h3>
    <p>Sed ut perspiciatis unde omnis iste natus error sit voluptatem accusantium doque laudantium, totam rem aperiam, eaque ipsa quae ab illo inventore veritatis et quasi architecto beatae</p>
  </div>
  <div class="service" style="left:768px">
    <div class="icon"><svg width="54" height="54" viewBox="0 0 54 54" fill="none" stroke="#2a2a2a" stroke-width="2.4"><circle cx="27" cy="14" r="6"/><circle cx="14" cy="20" r="5"/><circle cx="40" cy="20" r="5"/><path d="M18 44V30c0-4 4-7 9-7s9 3 9 7v14"/><path d="M6 44V33c0-3 3-6 8-6M48 44V33c0-3-3-6-8-6"/></svg></div>
    <h3>Career Leadership</h3>
    <p>Sed ut perspiciatis unde omnis iste natus error sit voluptatem accusantium doque laudantium, totam rem aperiam, eaque ipsa quae ab illo inventore veritatis et quasi architecto beatae</p>
  </div>
</section>

<section class="request">
  <div class="request-photo" role="img" aria-label="City skyline in daylight behind the mentor"></div>
  <div class="request-person" role="img" aria-label="Mentor in a dark suit and sunglasses leaning on a rail"></div>
  <h2><b>REQUEST</b> A FREE QUOTE</h2>
  <svg class="divider" style="left:142px;top:140px" viewBox="0 0 120 12"><line x1="8" y1="6" x2="112" y2="6" stroke="#e0222a" stroke-width="2"/><circle cx="6" cy="6" r="4" fill="none" stroke="#e0222a" stroke-width="2"/><circle cx="114" cy="6" r="4" fill="none" stroke="#e0222a" stroke-width="2"/></svg>
</section>
<div class="form-label" style="top:2170px">Name *</div>
<div class="form-input" style="top:2200px"></div>
<div class="form-label" style="top:2258px">Phone *</div>
<div class="form-input" style="top:2283px"></div>
<div class="form-label" style="top:2340px">Email *</div>
<div class="form-input" style="top:2365px"></div>
<div class="form-label" style="top:2420px">Event Date(s) of Interest *</div>
<div class="form-input" style="top:2448px;height:40px;font-size:13px;padding:11px 16px;color:#555">Please select
  <svg class="abs" style="right:12px;top:12px" width="10" height="16" viewBox="0 0 10 16"><path d="M1 6l4-4 4 4M1 10l4 4 4-4" stroke="#333" stroke-width="1.6" fill="none"/></svg>
</div>
<div class="btn submit-btn">SUBMIT</div>

<section class="news">
  <h2 class="section-title"><b>LATEST</b> NEWS</h2>
  <svg class="divider" style="top:142px" viewBox="0 0 120 12"><line x1="8" y1="6" x2="112" y2="6" stroke="#e0222a" stroke-width="2"/><circle cx="6" cy="6" r="4" fill="none" stroke="#e0222a" stroke-width="2"/><circle cx="114" cy="6" r="4" fill="none" stroke="#e0222a" stroke-width="2"/></svg>

  <div class="news-card" style="left:147px">
    <div class="tilt-frame" style="transform:rotate(-4deg)"><div role="img" aria-label="Speaker addressing a large audience in a hall" style="position:absolute;inset:10px;background:linear-gradient(180deg,#6b5a4c 0%,#3a302b 55%,#8a7462 100%)"></div></div>
    <h3>QUIS AUTEM VEL EUM IURE<br>DERIT QUI IN EA VOL</h3>
    <div class="news-date"><svg width="14" height="14" viewBox="0 0 14 14"><rect x="1" y="2.5" width="12" height="10.5" fill="none" stroke="#e0222a" stroke-width="1.6"/><path d="M1 6h12M4 1v3M10 1v3" stroke="#e0222a" stroke-width="1.6"/></svg>October 17, 2019</div>
  </div>
  <div class="news-card" style="left:463px">
    <div class="tilt-frame" style="transform:rotate(-4deg)"><div role="img" aria-label="Mentor greeting people at an event" style="position:absolute;inset:10px;background:linear-gradient(180deg,#5b4b44 0%,#2d2a2c 50%,#4a5468 100%)"></div></div>
    <h3>QUIS AUTEM VEL EUM IURE<br>DERIT QUI IN EA VOL</h3>
    <div class="news-date"><svg width="14" height="14" viewBox="0 0 14 14"><rect x="1" y="2.5" width="12" height="10.5" fill="none" stroke="#e0222a" stroke-width="1.6"/><path d="M1 6h12M4 1v3M10 1v3" stroke="#e0222a" stroke-width="1.6"/></svg>October 17, 2019</div>
  </div>
  <div class="news-card" style="left:780px">
    <div class="tilt-frame" style="transform:rotate(4deg)"><div role="img" aria-label="Colourful street mural beside a parked car" style="position:absolute;inset:10px;background:linear-gradient(90deg,#3f7fb0 0%,#d9a33a 35%,#b8473c 65%,#6a6a70 100%)"></div></div>
    <h3>QUIS AUTEM VEL EUM IURE<br>DERIT QUI IN EA VOL</h3>
    <div class="news-date"><svg width="14" height="14" viewBox="0 0 14 14"><rect x="1" y="2.5" width="12" height="10.5" fill="none" stroke="#e0222a" stroke-width="1.6"/><path d="M1 6h12M4 1v3M10 1v3" stroke="#e0222a" stroke-width="1.6"/></svg>October 17, 2019</div>
  </div>
</section>

<section class="testimonial">
  <svg class="abs" style="left:155px;top:150px" width="20" height="36" viewBox="0 0 20 36"><path d="M16 3L4 18l12 15" stroke="#fff" stroke-width="3.5" fill="none"/></svg>
  <svg class="abs" style="left:1025px;top:150px" width="20" height="36" viewBox="0 0 20 36"><path d="M4 3l12 15L4 33" stroke="#fff" stroke-width="3.5" fill="none"/></svg>
  <div class="avatar" role="img" aria-label="Portrait of a client giving a testimonial"></div>
  <div class="qmark" style="left:440px;top:60px">“</div>
  <div class="qmark" style="left:880px;top:170px">”</div>
  <blockquote>Aociosqu ad litora torquent per conubia nostra per inceptos hymenaeos Proin nulla arcu nonummy luctus dictum eget fermentum et lorem Nunc porta convallis pede</blockquote>
  <div class="author">Dorian Kessler,<br>vKeenstride</div>
</section>

<footer class="site-footer">
  <div class="brand"><span class="brand-mark"></span>KEENSTRIDE</div>
  <span class="social" style="left:143px"></span>
  <span class="social" style="left:183px"></span>
  <span class="social" style="left:223px"></span>
  <span class="social" style="left:263px"></span>

  <div class="foot-title" style="left:360px">Contact Us</div>
  <div class="foot-item" style="top:110px">
    <svg width="26" height="26" viewBox="0 0 26 26"><rect x="1" y="1" width="24" height="24" fill="none" stroke="#333" stroke-width="1.3"/><path d="M13 6a4.5 4.5 0 0 0-4.5 4.5c0 3.5 4.5 9 4.5 9s4.5-5.5 4.5-9A4.5 4.5 0 0 0 13 6z" fill="none" stroke="#333" stroke-width="1.3"/><circle cx="13" cy="10.5" r="1.6" fill="#333"/></svg>
    <div>vKeenstride<br>782 Larkmere Avenue, 9th floor<br>Riverton, NY 10462</div>
  </div>
  <div class="foot-item" style="top:190px">
    <svg width="26" height="26" viewBox="0 0 26 26"><rect x="1" y="1" width="24" height="24" fill="none" stroke="#333" stroke-width="1.3"/><path d="M9 7c.7-.7 1.4-.7 2 0l1.4 2c.4.7.3 1.3-.3 1.8l-.9.7c.7 1.6 1.9 2.9 3.4 3.6l.7-.9c.4-.6 1.1-.7 1.8-.3l2 1.3c.7.5.7 1.2 0 1.9l-1 1c-1 .9-2.7.7-4.7-.8-2.2-1.6-4-3.8-4.9-5.9-.7-1.7-.7-3.1.1-3.9z" fill="none" stroke="#333" stroke-width="1.2"/></svg>
    <div>Call us today:<br>(417) 620-3184</div>
  </div>
  <div class="foot-item" style="top:258px">
    <svg width="26" height="26" viewBox="0 0 26 26"><rect x="1" y="1" width="24" height="24" fill="none" stroke="#333" stroke-width="1.3"/><rect x="6" y="8" width="14" height="10" fill="none" stroke="#333" stroke-width="1.3"/><path d="M6 8l7 6 7-6" fill="none" stroke="#333" stroke-width="1.3"/></svg>
    <div>Email :<br>info@vkeenstride.net</div>
  </div>

  <div class="foot-title" style="left:610px">Sign up for newsletter</div>
  <div class="foot-text">Excepteur sint occaecat cupidatat non proident, sunt in culpa qui officia deserunt</div>
  <div class="foot-input">Enter email</div>

  <div class="foot-title" style="left:923px">Quick Links</div>
  <ul class="quick"><li>Home</li><li>Summit Circle</li><li>Hire RM</li><li>About us</li><li>Contact us</li></ul>
</footer>
<div class="btn foot-btn">SUBSCRIBE</div>

<footer class="copyright">© Copyright 2019 vKeenstride. All Rights Reserved.</footer>

</body>
</html>
```